Pedicure Menu with 8 Scent Options

This design will be for a single page menu (front/back) that will display multiple different scent variations of a product. The purpose of this menu is to display to clients and show them the available options and benefits of each option.
The menu will be double sided.
The front page will include a header including brand logo and product name, and a total of 8 different scents including imagery and descriptive text.
The design should include the text provided for each scent. The design should have a layout that is structured/organized, easy to read, and has bright imagery that represents each scent.
An example is a modular layout using boxes that highlight a different scent within each box. Lavender scent should include aesthetic images of lavender flower and/or the color purple.
The back page will include brand logo, overall product description, and additional brief text that explains each step of the product.
The final size of the design should be 8.5"x11", produced in InDesign format, with all layers editable for future changes.
NOTE: Please carefully review the attached design brief that includes additional information, and all necessary text to include in the design.
Target Market(s)
Beauty/Spa Clients
Industry/Entity Type
Beauty
Requirements
Must have
- Bright and Vivid Imagery/Illustrations
Nice to have
- Background design that utilizes, lines, shapes, or other elements.

```html
<!DOCTYPE html>
<html lang="en">
<head>
<meta charset="utf-8">
<title>Deluxe Pedicure – Pick Your Pedicure</title>
<link rel="stylesheet" href="https://fonts.googleapis.com/css2?family=Great+Vibes&family=Exo+2:wght@500&family=Montserrat:wght@500;800&family=Source+Sans+3:wght@400&display=swap">
<style>
  :root {
    --page-bg: #fbeef0;
    --card-bg: #ffffff;
    --card-line: #f3a9c0;
    --hot-pink: #f34c80;
    --title-pink: #ee4a86;
    --blob-deep: #f66e99;
    --blob-soft: #f8a9c0;
    --blob-pale: #fbd3df;
    --ink: #1f1a1c;
    --body-ink: #2a2325;
  }
  * { margin: 0; padding: 0; box-sizing: border-box; }
  html, body { width: 927px; height: 1200px; overflow: hidden; background: var(--page-bg); }
  .menu-page { position: relative; width: 927px; height: 1200px; overflow: hidden; background: var(--page-bg); font-family: "Source Sans 3", Arial, sans-serif; color: var(--body-ink); }

  .header-shapes, .footer-wave { position: absolute; left: 0; width: 927px; }
  .header-shapes { top: 0; height: 202px; }
  .footer-wave { bottom: 0; height: 75px; }

  .line-art { position: absolute; background: rgba(255,255,255,0.35); border-radius: 40%; }
  .line-art--left { left: 30px; top: 0; width: 140px; height: 80px; }
  .line-art--right { left: 605px; top: 0; width: 300px; height: 118px; }

  .brand { position: absolute; left: 47px; top: 120px; display: flex; align-items: center; gap: 8px; }
  .brand-name { font-family: "Montserrat", Arial, sans-serif; font-weight: 500; font-size: 44px; letter-spacing: 1px; color: var(--ink); line-height: 1; }
  .brand-mark { width: 8px; height: 8px; background: var(--ink); border-radius: 50%; }

  .title-panel { position: absolute; left: 267px; top: 0; width: 268px; height: 233px; background: var(--hot-pink); box-shadow: 0 4px 12px rgba(0,0,0,0.18); }
  .title-panel__script { position: absolute; left: 24px; top: 48px; font-family: "Great Vibes", cursive; font-size: 70px; line-height: 54px; color: #fff; white-space: nowrap; }
  .title-panel__steps { position: absolute; right: 26px; top: 176px; font-family: "Montserrat", Arial, sans-serif; font-weight: 800; font-size: 27px; letter-spacing: 5px; color: var(--ink); }

  .pick-tag { position: absolute; left: 659px; top: 131px; width: 280px; height: 41px; background: #fff; border: 1.5px solid var(--ink); border-radius: 22px 0 0 22px; font-family: "Montserrat", Arial, sans-serif; font-weight: 800; font-size: 14px; letter-spacing: 3px; color: var(--ink); line-height: 38px; padding-left: 29px; white-space: nowrap; }

  .scent-card { position: absolute; left: 118px; top: 253px; width: 699px; height: 876px; background: var(--card-bg); border: 1px solid var(--card-line); }

  .scent-art { position: absolute; border-radius: 45%; opacity: 0.85; }

  .scent-title { position: absolute; font-family: "Exo 2", Arial, sans-serif; font-weight: 500; font-size: 22px; color: var(--title-pink); line-height: 1; letter-spacing: 0.8px; white-space: nowrap; }
  .scent-title::first-letter { font-size: 27px; }
  .scent-title .dots { color: var(--ink); font-size: 20px; letter-spacing: 5px; margin: 0 10px; }
  .scent-text { position: absolute; font-size: 12.3px; line-height: 14.6px; white-space: nowrap; }
  .scent-text .line { display: block; }
  .scent-text--left { text-align: left; }
  .scent-text--right { text-align: right; }
  .scent-text .line--justify { white-space: normal; text-align: justify; text-align-last: justify; }
</style>
</head>
<body>
<main class="menu-page">

  <svg class="header-shapes" viewBox="0 0 927 202" aria-hidden="true">
    <path d="M0 48 C60 40 110 70 140 110 C175 150 230 150 267 202 L0 202 Z" fill="var(--blob-deep)"/>
    <path d="M100 202 C140 150 200 140 267 120 L267 202 Z" fill="var(--blob-pale)"/>
    <path d="M535 190 C620 170 700 150 760 160 C820 170 860 185 927 180 L927 202 L535 202 Z" fill="var(--blob-soft)"/>
    <path d="M760 202 C740 150 740 80 800 40 C840 15 890 10 927 18 L927 202 Z" fill="var(--blob-deep)"/>
  </svg>
  <div class="line-art line-art--left" role="img" aria-label="Line drawing of blossoms and leaves"></div>
  <div class="line-art line-art--right" role="img" aria-label="Line drawing of tulips and leafy sprigs"></div>

  <div class="brand"><span class="brand-name">Sevlia</span><span class="brand-mark"></span></div>

  <section class="title-panel">
    <div class="title-panel__script">Deluxe<br>Pedicure</div>
    <div class="title-panel__steps">4-STEP</div>
  </section>

  <div class="pick-tag">PICK YOUR PEDICURE</div>

  <section class="scent-card"></section>

  <div class="scent-art" style="left:80px;top:247px;width:110px;height:146px;background:linear-gradient(160deg,#9c7bc4,#e9def0);" role="img" aria-label="Watercolour lavender sprigs"></div>
  <div class="scent-art" style="left:714px;top:321px;width:134px;height:154px;background:radial-gradient(circle,#f59a44,#4f8a5c);" role="img" aria-label="Watercolour mandarin branch with fruit"></div>
  <div class="scent-art" style="left:71px;top:450px;width:140px;height:135px;background:radial-gradient(circle,#f4efe0,#5c7b55);" role="img" aria-label="Watercolour jasmine blossoms"></div>
  <div class="scent-art" style="left:730px;top:579px;width:143px;height:118px;background:radial-gradient(circle,#f2c17f,#7aa26b);" role="img" aria-label="Watercolour melons and cucumber"></div>
  <div class="scent-art" style="left:60px;top:651px;width:140px;height:164px;background:radial-gradient(circle,#6fae9a,#3c4a44);" role="img" aria-label="Watercolour mint leaves"></div>
  <div class="scent-art" style="left:727px;top:788px;width:124px;height:132px;background:radial-gradient(circle,#d9705f,#5e7d7a);" role="img" aria-label="Watercolour rose"></div>
  <div class="scent-art" style="left:63px;top:865px;width:137px;height:137px;background:linear-gradient(160deg,#f4c04a,#f7ecd6);" role="img" aria-label="Watercolour jars of milk and honey"></div>
  <div class="scent-art" style="left:730px;top:1002px;width:137px;height:137px;background:radial-gradient(circle,#a6b84e,#3f6d35);" role="img" aria-label="Watercolour green tea leaves"></div>

  <h2 class="scent-title" style="left:213px;top:302px;">Lavender<span class="dots">••••</span></h2>
  <p class="scent-text scent-text--left" style="left:213px;top:329px;">
    <span class="line">Melt away the stresses of the day with a delicate, sweet smell that is floral and woodsy</span>
    <span class="line">at the same time. Lavender is a calming scent for relaxation that puts us in a better</span>
    <span class="line">mood and helps create a sense of tranquility and peacefulness.</span>
  </p>

  <h2 class="scent-title" style="right:220px;top:403px;"><span class="dots">••••</span>Mandarin</h2>
  <p class="scent-text scent-text--right" style="left:322px;top:430px;width:388px;">
    <span class="line line--justify">Uplift your senses with a fruity and sweet aroma that promotes clarity,</span>
    <span class="line line--justify">radiance and a smooth, even skin tone. A citrus blend of essential oils works</span>
    <span class="line">great to polish dull skin, reduce wrinkles, and correct spots.</span>
  </p>

  <h2 class="scent-title" style="left:213px;top:501px;">Jasmine<span class="dots">&nbsp;••••</span></h2>
  <p class="scent-text scent-text--left" style="left:215px;top:532px;">
    <span class="line">Embrace the warmth of a rich and sensual floral scent that boosts your energy levels and helps</span>
    <span class="line">make your day better and brighter. A symbol of purity, love, and beauty – Jasmine helps to reduce</span>
    <span class="line">exhaustion, nervousness, and stress.</span>
  </p>

  <h2 class="scent-title" style="right:213px;top:607px;"><span class="dots">••••</span>Cucumber-Melon</h2>
  <p class="scent-text scent-text--right" style="left:329px;top:638px;width:385px;">
    <span class="line line--justify">Jump into a refreshing blend of crisp cucumber, watery honeydew, and</span>
    <span class="line line--justify">summer cantaloupe. Perfect for capturing the essence of a summer day.</span>
    <span class="line">Bamboo and aloe extract help cool your skin after a day in the sun.</span>
  </p>

  <h2 class="scent-title" style="left:213px;top:712px;">Mint<span class="dots">&nbsp;••••</span></h2>
  <p class="scent-text scent-text--left" style="left:213px;top:741px;">
    <span class="line">Rejuvenate your body with a cool mix of peppermint and spearmint that prevents skin damage,</span>
    <span class="line">alleviates inflamed skin, and acts as a splash of tonic for the senses. Infused with eucalyptus to</span>
    <span class="line">leave you clean, cool, and crisp.</span>
  </p>

  <h2 class="scent-title" style="right:215px;top:824px;"><span class="dots">••••</span>Rose</h2>
  <p class="scent-text scent-text--right" style="left:330px;top:853px;width:384px;">
    <span class="line">Fall in love with a delicate floral twist of spicy and sweet that nourishes your</span>
    <span class="line">skin and calms the mind. Essential oils help to reduce fine lines and protect</span>
    <span class="line">the skin from UV damage.</span>
  </p>

  <h2 class="scent-title" style="left:213px;top:922px;">Milk and Honey<span class="dots">••••</span></h2>
  <p class="scent-text scent-text--left" style="left:213px;top:948px;">
    <span class="line">Discover one of nature’s most luxurious skin cleansers and softeners. Creamy milk is full of rich</span>
    <span class="line">essential vitamins that supply abundant moisture and improves skin elasticity. Sweet honey</span>
    <span class="line">contains antioxidants and other nutrients that slow down skin aging.</span>
  </p>

  <h2 class="scent-title" style="right:216px;top:1027px;"><span class="dots">••••</span>Green Tea</h2>
  <p class="scent-text scent-text--right" style="left:337px;top:1053px;width:378px;">
    <span class="line">Restore a sense of serenity with fragrant green tea extract that helps to relax</span>
    <span class="line line--justify">the mind, reduces redness and swelling, and leaves the skin feeling</span>
    <span class="line line--justify">hydrated, silky, and smooth. A natural detoxification that will supplies</span>
    <span class="line">abundant moisture to the skin.</span>
  </p>

  <svg class="footer-wave" viewBox="0 0 927 75" aria-hidden="true">
    <path d="M0 20 C200 8 420 30 560 60 L560 75 L0 75 Z" fill="var(--blob-pale)"/>
    <path d="M0 22 C150 5 330 10 390 45 C410 60 400 75 400 75 L0 75 Z" fill="var(--blob-deep)"/>
    <path d="M560 75 C650 40 800 50 927 68 L927 75 Z" fill="var(--blob-pale)"/>
  </svg>
</main>
</body>
</html>
```